Quick Straightforward Billboard Redesign

- Design billboard sized for 10 foot' x 36' foot width live area size and please include bleeds 6" around all sides
- Exact blue color match is imperative in headline, logo, phone number bubble or wherever used. C-83 / M-45 / Y-1 / K-0-
- What I hope to illustrate is that our company offers the best porch screening in the area area, in regards to quality, expertise, durability, storms proof, but we do not build screen porches.
- Current board is attached below from previous designer, and as you can see sizing was off, white space on edges make it appear to be sized incorrectly.
- I also attached my own little mock up idea well well if it helps, favorite image, logo, headline, etc and ideas perhaps on expanding or making this better?

Thanks so much!

Target Market(s)

Drivers and passengers, Southeastern NC, are of immense new construction and high end homes.

Industry/Entity Type

Construction

Colors
0054AA
0677BA
7BADD7
CADEEF
E8F1F8

Requirements
Must have
• Blue color matching
Nice to have
• Design spins or other thoughts on my little mock up

```html
<!DOCTYPE html>
<html lang="en">
<head>
<meta charset="utf-8">
<title>Porch Screening Billboard</title>
<link href="https://fonts.googleapis.com/css2?family=Anton&display=swap" rel="stylesheet">
<style>
  :root {
    --brand-blue: #1466b4;
    --brand-green: #2bb35a;
    --accent-sky: #22b8e8;
    --board-white: #ffffff;
    --backdrop: #b3b3b3;
    --photo-sky: #7fb6e6;
    --photo-deck: #9c8f80;
  }
  * { margin: 0; padding: 0; box-sizing: border-box; }
  html, body {
    width: 1036px;
    height: 1200px;
    overflow: hidden;
    background: var(--backdrop);
  }
  .billboard {
    position: absolute;
    left: 48px;
    top: 455px;
    width: 940px;
    height: 290px;
    background: var(--board-white);
    box-shadow: 0 22px 18px -10px rgba(0,0,0,0.35);
    overflow: hidden;
    font-family: "Anton", "Arial Narrow", sans-serif;
  }
  .headline {
    position: absolute;
    left: 21px;
    top: 40px;
    line-height: 1.08;
    letter-spacing: -0.5px;
  }
  .headline-primary {
    display: block;
    font-size: 70px;
    color: var(--brand-blue);
  }
  .headline-secondary {
    display: block;
    font-size: 64px;
    color: var(--brand-green);
  }
  .brand {
    position: absolute;
    left: 22px;
    top: 222px;
    display: flex;
    align-items: center;
    gap: 10px;
  }
  .brand-dot {
    width: 22px;
    height: 22px;
    border-radius: 50%;
    background: var(--accent-sky);
  }
  .brand-name {
    font-size: 26px;
    color: var(--brand-blue);
    letter-spacing: 0.3px;
  }
  .porch-photo {
    position: absolute;
    left: 640px;
    top: 0;
    width: 300px;
    height: 290px;
    clip-path: polygon(52px 0, 100% 0, 100% 100%, 0 100%);
    background: linear-gradient(180deg, #e9edf0 0%, #e9edf0 30%, var(--photo-sky) 30%, #cfe2c4 50%, #8aa76a 58%, var(--photo-deck) 75%, #6d5f52 100%);
  }
  .phone-tag {
    position: absolute;
    left: 728px;
    top: 235px;
    width: 212px;
    height: 38px;
    background: var(--brand-blue);
    clip-path: polygon(10px 0, 100% 0, 100% 100%, 0 100%);
    display: flex;
    align-items: center;
    gap: 8px;
    padding-left: 22px;
    color: var(--board-white);
    font-size: 25px;
    border-top: 2px solid var(--board-white);
  }
  .phone-icon { width: 22px; height: 22px; }
</style>
</head>
<body>
  <section class="billboard">
    <h1 class="headline">
      <span class="headline-primary">Screen Your Porch.</span>
      <span class="headline-secondary">Built for the Coast</span>
    </h1>

    <div class="brand">
      <span class="brand-dot"></span>
      <span class="brand-name">TIDEWATER SCREENING</span>
    </div>

    <div class="porch-photo" role="img" aria-label="Photo of a covered screened porch with wicker seating overlooking a lake"></div>

    <div class="phone-tag">
      <svg class="phone-icon" viewBox="0 0 24 24" aria-hidden="true">
        <path fill="#ffffff" d="M6.6 10.8c1.4 2.8 3.8 5.1 6.6 6.6l2.2-2.2c.3-.3.7-.4 1-.2 1.1.4 2.3.6 3.6.6.6 0 1 .4 1 1V20c0 .6-.4 1-1 1C10.6 21 3 13.4 3 4c0-.6.4-1 1-1h3.5c.6 0 1 .4 1 1 0 1.3.2 2.5.6 3.6.1.3 0 .7-.2 1l-2.3 2.2z"/>
      </svg>
      <span class="phone-number">910.555.0148</span>
    </div>
  </section>
</body>
</html>
```